Fun spin on a Wanted poster

We are launching a new campaign for a first home building company Brightlane Homes. I require a wanted poster to use in the marketing material. The design should use only the colours used in the logo, this include black. Concentrate on using the bright colours.

The brand is youthful and energetic so have so fun with the design. It needs to engage the viewer and have them wanting to look into further details.

Attached is logo in full colour and monochromatic. Would prefer the full colour version used. Characters also attached.

Poster must include
Wanted
First Home Buyers
Image - Use provided characters or similar
Reward
Quality, Affordable, New homes
Contact Brightlane Homes on ########### for further information
www.brightlanehomes.com.au

A3 size

Final design will need to be supplied as editable adobe illustrator file. Added Thursday, October 16, 2014

Industry/Entity Type

Marketing

Font styles to use
Other font styles liked:
• Soho Std

Requirements
Must have
• BLH Characters and colours. Soho Fonts

```html
<!DOCTYPE html>
<html lang="en">
<head>
<meta charset="utf-8">
<title>Wanted: First Home Buyers – Brightlane Homes</title>
<link rel="stylesheet" href="https://fonts.googleapis.com/css2?family=Audiowide&family=Baloo+2:wght@800&family=Roboto+Condensed:wght@700&display=swap">
<style>
  :root {
    --olive: #aebd4e;
    --olive-light: #d4e07a;
    --olive-dark: #6f7a26;
    --sky: #6fb6e8;
    --yellow: #ffef3a;
    --grey-dark: #6f6f6f;
    --floor: #d6d6d6;
    --green: #2ea84f;
    --green-bush: #45b86a;
    --ink: #1a1a1a;
    --text-grey: #4a4a4a;
    --navy: #2a2f8f;
    --hair-dark: #3a3a3a;
    --suit-grey: #9a9a9a;
    --dress-red: #e4262b;
    --hair-blonde: #f5e35a;
    --white: #ffffff;
  }
  html, body {
    margin: 0;
    padding: 0;
    overflow: hidden;
    background: var(--white);
  }
  .poster {
    position: relative;
    width: 851px;
    height: 1200px;
    overflow: hidden;
    background: var(--floor);
  }
  .poster__header {
    position: absolute;
    inset: 0 0 auto 0;
    height: 420px;
    background: radial-gradient(ellipse at 50% 35%, #a3a3a3 0%, #858585 55%, var(--grey-dark) 100%);
  }
  .headline {
    position: absolute;
    left: 0;
    width: 100%;
    margin: 0;
    text-align: center;
    font-family: "Audiowide", sans-serif;
    font-weight: 400;
    color: var(--olive);
    text-shadow:
      0 0 14px rgba(230, 255, 120, .55),
      1px 1px 0 var(--olive-light),
      3px 4px 0 var(--olive-dark),
      5px 7px 8px rgba(0, 0, 0, .35);
  }
  .headline--wanted {
    top: 14px;
    font-size: 148px;
    letter-spacing: 2px;
    line-height: 1;
    text-transform: uppercase;
  }
  .headline--buyers {
    top: 188px;
    font-size: 74px;
    line-height: 1;
  }
  .scene {
    position: absolute;
    left: 0;
    top: 0;
    width: 851px;
    height: 1200px;
  }
  .tagline {
    position: absolute;
    left: 0;
    top: 302px;
    width: 851px;
    margin: 0;
    text-align: center;
    font-family: "Baloo 2", sans-serif;
    font-weight: 800;
    font-size: 54px;
    line-height: 1;
    color: var(--ink);
    letter-spacing: -0.5px;
    transform: rotate(1.2deg);
  }
  .characters {
    position: absolute;
    left: 238px;
    top: 478px;
    width: 400px;
    height: 430px;
    border-radius: 46% 46% 18% 18%;
    background: linear-gradient(100deg,
      var(--hair-dark) 0%,
      var(--suit-grey) 30%,
      #e9e9e9 48%,
      var(--hair-blonde) 58%,
      var(--dress-red) 78%,
      var(--dress-red) 100%);
    box-shadow: 0 18px 24px rgba(0, 0, 0, .18);
  }
  .reward-sign {
    position: absolute;
    left: 530px;
    top: 426px;
    font-family: "Roboto Condensed", sans-serif;
    font-weight: 700;
    font-size: 27px;
    color: var(--ink);
    letter-spacing: -0.5px;
  }
  .welcome-mat {
    position: absolute;
    left: 263px;
    top: 928px;
    width: 342px;
    height: 70px;
    border-radius: 6px;
    background: var(--green);
    display: flex;
    align-items: center;
    justify-content: center;
    transform: rotate(180deg);
    font-family: "Baloo 2", sans-serif;
    font-weight: 800;
    font-size: 54px;
    color: var(--white);
    line-height: 1;
  }
  .brand {
    position: absolute;
    display: flex;
    align-items: center;
    gap: 6px;
    font-family: "Baloo 2", sans-serif;
    font-weight: 800;
    color: var(--sky);
    line-height: 1;
    white-space: nowrap;
  }
  .brand__square {
    width: 14px;
    height: 14px;
    background: var(--yellow);
    flex: none;
  }
  .brand--door {
    left: 26px;
    top: 620px;
    font-size: 19px;
  }
  .brand--footer {
    right: 14px;
    top: 34px;
    font-size: 17px;
  }
  .footer {
    position: absolute;
    left: 0;
    top: 1092px;
    width: 851px;
    height: 108px;
    background: var(--white);
  }
  .footer__icon {
    position: absolute;
  }
  .footer__icon--phone { left: 42px; top: 6px; }
  .footer__icon--mouse { left: 176px; top: 42px; }
  .contact {
    position: absolute;
    left: 108px;
    top: 10px;
    margin: 0;
    font-family: "Roboto Condensed", sans-serif;
    font-weight: 700;
    font-size: 24px;
    color: var(--text-grey);
    text-shadow: 2px 2px 2px rgba(0, 0, 0, .3);
    white-space: nowrap;
  }
  .website {
    position: absolute;
    left: 262px;
    top: 46px;
    margin: 0;
    font-family: "Roboto Condensed", sans-serif;
    font-weight: 700;
    font-size: 24px;
    color: var(--text-grey);
    text-shadow: 2px 2px 2px rgba(0, 0, 0, .3);
  }
</style>
</head>
<body>
<main class="poster">
  <div class="poster__header"></div>

  <svg class="scene" viewBox="0 0 851 1200" aria-hidden="true">
    <defs>
      <linearGradient id="doorLeft" x1="0" x2="1">
        <stop offset="0" stop-color="#a9a9a9"/>
        <stop offset=".6" stop-color="#cfcfcf"/>
        <stop offset="1" stop-color="#bdbdbd"/>
      </linearGradient>
      <linearGradient id="doorRight" x1="1" x2="0">
        <stop offset="0" stop-color="#a9a9a9"/>
        <stop offset=".6" stop-color="#cfcfcf"/>
        <stop offset="1" stop-color="#bdbdbd"/>
      </linearGradient>
      <linearGradient id="sky" x1="0" y1="0" x2="0" y2="1">
        <stop offset="0" stop-color="#5aa7e0"/>
        <stop offset="1" stop-color="#bfdff5"/>
      </linearGradient>
      <linearGradient id="banner" x1="0" y1="0" x2="0" y2="1">
        <stop offset="0" stop-color="#fffde0"/>
        <stop offset=".45" stop-color="#fff35a"/>
        <stop offset="1" stop-color="#ffe81a"/>
      </linearGradient>
    </defs>

    <path d="M0 360 Q425 330 851 360 L851 440 Q425 400 0 440 Z" fill="#c9c9c9"/>

    <rect x="170" y="420" width="520" height="230" fill="url(#sky)"/>
    <rect x="170" y="638" width="520" height="8" fill="var(--ink)"/>
    <rect x="170" y="646" width="520" height="420" fill="var(--floor)"/>
    <path d="M170 1066 L690 1066 L690 1092 L170 1092 Z" fill="#c4c4c4"/>

    <rect x="646" y="450" width="14" height="200" fill="#e4e4e4" stroke="#9a9a9a" stroke-width="1.5"/>

    <path d="M160 1010 L160 800 Q200 740 250 790 L250 1010 Z" fill="var(--green-bush)"/>
    <path d="M690 1010 L690 800 Q650 740 610 790 L610 1010 Z" fill="var(--green-bush)"/>

    <path d="M0 400 L180 400 Q240 410 236 470 L236 1060 Q200 1080 150 1075 L0 1075 Z" fill="url(#doorLeft)"/>
    <path d="M851 400 L700 400 Q686 410 688 470 L688 560 Q640 600 640 660 L640 1060 Q680 1080 730 1075 L851 1075 Z" fill="url(#doorRight)"/>

    <path d="M498 436 L520 416 L698 420 L694 476 L520 470 Z" fill="var(--white)" stroke="#8a8a8a" stroke-width="2"/>

    <path d="M0 312 Q425 268 851 312 L851 390 Q425 350 0 392 Z" fill="url(#banner)"/>
    <path d="M0 312 Q425 268 851 312" fill="none" stroke="#fffbd0" stroke-width="3"/>
  </svg>

  <h1 class="headline headline--wanted">Wanted</h1>
  <h2 class="headline headline--buyers">first home buyers</h2>
  <p class="tagline">quality ~ affordable ~ new homes</p>

  <div class="reward-sign">REWARD $T</div>

  <div class="characters" role="img" aria-label="Illustrated young couple holding hands in the doorway, he with dark spiky hair in a white jacket and blue tie, she with long blonde hair in a red gown"></div>

  <div class="welcome-mat">welcome</div>

  <div class="brand brand--door"><span class="brand__square"></span>Brightlane Homes</div>

  <footer class="footer">
    <svg class="footer__icon footer__icon--phone" width="44" height="44" viewBox="0 0 44 44" aria-hidden="true">
      <circle cx="22" cy="22" r="20" fill="var(--white)" stroke="var(--navy)" stroke-width="3"/>
      <path d="M15 11 Q10 14 13 22 Q17 31 26 34 Q31 35 33 31 L28 26 L24 28 Q19 25 17 19 L20 16 Z" fill="var(--navy)"/>
    </svg>
    <svg class="footer__icon footer__icon--mouse" width="56" height="46" viewBox="0 0 56 46" aria-hidden="true">
      <ellipse cx="20" cy="28" rx="15" ry="16" fill="var(--navy)"/>
      <path d="M20 13 L20 28 M6 27 L34 27" stroke="var(--white)" stroke-width="2"/>
      <path d="M33 20 Q44 2 52 14" fill="none" stroke="var(--navy)" stroke-width="3"/>
    </svg>
    <p class="contact">Contact Brightlane Homes on ######## for further information</p>
    <p class="website">www.brightlanehomes.com.au</p>
    <div class="brand brand--footer"><span class="brand__square"></span>Brightlane Homes</div>
  </footer>
</main>
</body>
</html>
```